KORBALT

The business want a professional looking business card. We have a scetch we will add but want the extra upgrade, and would like more suggestions for variations of our business cards.

```html
<!DOCTYPE html>
<html lang="en">
<head>
<meta charset="utf-8">
<title>KORBALT Business Card</title>
<link rel="stylesheet" href="https://fonts.googleapis.com/css2?family=Playfair+Display:wght@700&family=Montserrat:wght@500&display=swap">
<style>
  :root {
    --backdrop: #808080;
    --ink: #6b4520;
    --paper-light: #fbfaf6;
    --paper-warm: #e8e1d6;
    --gold-deep: #c9a24f;
    --gold-mid: #f0cf7a;
    --gold-light: #fbe3a0;
    --white: #ffffff;
  }
  * { margin: 0; padding: 0; box-sizing: border-box; }
  html, body { width: 1200px; height: 1027px; overflow: hidden; background: var(--backdrop); }
  .canvas { position: relative; width: 1200px; height: 1027px; }
  .card { position: absolute; left: 261px; width: 679px; height: 397px; overflow: hidden; }
  .card-front {
    top: 87px;
    background: linear-gradient(20deg, var(--paper-warm) 0%, #f2eee7 45%, var(--paper-light) 100%);
  }
  .card-back {
    top: 543px;
    background: linear-gradient(150deg,
      var(--gold-deep) 0%, var(--gold-mid) 12%, var(--gold-light) 24%, var(--gold-mid) 34%,
      var(--gold-deep) 48%, var(--gold-mid) 60%, var(--gold-light) 72%, var(--gold-mid) 84%, var(--gold-deep) 100%);
  }
  .ribbons { position: absolute; inset: 0; width: 679px; height: 397px; }
  .company-name {
    position: absolute; left: 45px; top: 60px;
    font-family: "Playfair Display", serif; font-weight: 700;
    font-size: 36px; letter-spacing: 0.5px; color: var(--ink); white-space: nowrap;
  }
  .role {
    position: absolute; left: 45px; top: 101px;
    font-family: "Montserrat", sans-serif; font-weight: 500;
    font-size: 26px; color: var(--ink);
  }
  .person {
    position: absolute; left: 45px; top: 127px;
    font-family: "Montserrat", sans-serif; font-weight: 500;
    font-size: 15px; color: var(--ink);
  }
  .contacts { position: absolute; left: 45px; top: 210px; list-style: none; }
  .contact { display: flex; align-items: center; height: 25px; margin-bottom: 12px; }
  .contact-icon {
    width: 25px; height: 25px; border-radius: 4px; background: var(--ink);
    display: flex; align-items: center; justify-content: center; margin-right: 14px;
  }
  .contact-text {
    font-family: "Montserrat", sans-serif; font-weight: 500;
    font-size: 22px; color: var(--ink);
  }
  .brand-name {
    position: absolute; left: 490px; width: 165px; top: 124px; text-align: center;
    font-family: "Playfair Display", serif; font-weight: 700;
    font-size: 32px; color: var(--ink);
  }
  .back-name {
    position: absolute; inset: 0; display: flex; align-items: center; justify-content: center;
    font-family: "Playfair Display", serif; font-weight: 700;
    font-size: 44px; letter-spacing: 2px; color: var(--white);
  }
</style>
</head>
<body>
<main class="canvas">
  <section class="card card-front">
    <svg class="ribbons" viewBox="0 0 679 397" aria-hidden="true">
      <defs>
        <linearGradient id="goldSheen" x1="0" y1="0" x2="1" y2="0">
          <stop offset="0" stop-color="#fbe3a0"/>
          <stop offset="0.3" stop-color="#c9a24f"/>
          <stop offset="0.55" stop-color="#fbe3a0"/>
          <stop offset="0.75" stop-color="#c9a24f"/>
          <stop offset="1" stop-color="#f0cf7a"/>
        </linearGradient>
        <linearGradient id="cornerSheen" x1="0" y1="0" x2="1" y2="1">
          <stop offset="0" stop-color="#f0cf7a"/>
          <stop offset="0.5" stop-color="#c9a24f"/>
          <stop offset="1" stop-color="#fbe3a0"/>
        </linearGradient>
      </defs>
      <path class="corner-ribbon" d="M0 0 H145 C80 15 25 55 0 102 Z" fill="url(#cornerSheen)"/>
      <path class="wave-band" d="M263 397 C360 330 470 315 560 302 C620 293 660 270 679 238 V317 C630 332 560 335 480 340 C400 345 340 360 300 397 Z" fill="url(#goldSheen)"/>
      <path class="wave-line" d="M335 397 C420 360 520 355 600 350 C640 347 665 342 679 339 V345 C660 350 630 355 590 357 C500 362 420 370 355 397 Z" fill="url(#goldSheen)"/>
    </svg>

    <h1 class="company-name">KORBALT HOLMVIK</h1>
    <p class="role">CEO &amp; Founder</p>
    <p class="person">Mats Olav Holmvik</p>

    <ul class="contacts">
      <li class="contact">
        <span class="contact-icon">
          <svg width="14" height="14" viewBox="0 0 24 24" aria-hidden="true"><path d="M6.6 10.8a15.1 15.1 0 0 0 6.6 6.6l2.2-2.2a1 1 0 0 1 1-.25 11.4 11.4 0 0 0 3.6.57 1 1 0 0 1 1 1V20a1 1 0 0 1-1 1A17 17 0 0 1 3 4a1 1 0 0 1 1-1h3.5a1 1 0 0 1 1 1c0 1.25.2 2.45.57 3.57a1 1 0 0 1-.25 1z" fill="#fff"/></svg>
        </span>
        <span class="contact-text">004791236540</span>
      </li>
      <li class="contact">
        <span class="contact-icon">
          <svg width="15" height="12" viewBox="0 0 24 18" aria-hidden="true"><rect x="1.5" y="1.5" width="21" height="15" rx="1.5" fill="none" stroke="#fff" stroke-width="2"/><path d="M2 2.5 12 10l10-7.5" fill="none" stroke="#fff" stroke-width="2"/></svg>
        </span>
        <span class="contact-text">korbalt.llc@mailbox.com</span>
      </li>
      <li class="contact">
        <span class="contact-icon">
          <svg width="15" height="15" viewBox="0 0 24 24" aria-hidden="true"><g fill="none" stroke="#fff" stroke-width="1.8"><circle cx="12" cy="12" r="10"/><ellipse cx="12" cy="12" rx="4.5" ry="10"/><path d="M2 12h20"/></g></svg>
        </span>
        <span class="contact-text">www.korbalt.llc</span>
      </li>
    </ul>

    <p class="brand-name">KORBALT</p>
  </section>

  <section class="card card-back">
    <p class="back-name">KORBALT</p>
  </section>
</main>
</body>
</html>
```